Business card for Chicago based Private Equity Company

We need a business card for our PE company called Crestline Holdings. We want a simple and clean, yet creative card design. The back side should reflect our logo. Also would like to see embossed ideas. Should reflect strength and growth. Our logo is attached. Also need editable file. Details are as follows for Business Card:

Dana Welmore Co-Founder 2750 Marlow Avenue Suite 410 Fernvale, IL 60914 http://www.crestlineholdingsllc.example (D) 630.555.0147 (C) 312.555.0182 (E) dw@crestlineholdingsllc.example

```html
<!DOCTYPE html>
<html lang="en">
<head>
<meta charset="utf-8">
<title>Crestline Holdings – Business Card</title>
<link href="https://fonts.googleapis.com/css2?family=Source+Sans+3:wght@400;600&display=swap" rel="stylesheet">
<style>
  :root {
    --backdrop: #dcdcdc;
    --card-white: #ffffff;
    --card-dark: #2e2e2e;
    --card-dark-back: #2b2b2b;
    --accent-blue: #1a8fd0;
    --text-grey: #555555;
    --title-grey: #666666;
    --emboss: #363636;
    --logo-white: #ffffff;
  }
  * { box-sizing: border-box; margin: 0; padding: 0; }
  html, body { width: 1200px; height: 1000px; overflow: hidden; }
  body {
    background: var(--backdrop);
    font-family: "Source Sans 3", "Myriad Pro", sans-serif;
    position: relative;
  }
  .card {
    position: absolute;
    left: 240px;
    width: 720px;
    height: 411px;
    overflow: hidden;
    box-shadow: 0 6px 18px rgba(0,0,0,0.25);
  }
  .card--front { top: 54px; background: var(--card-white); }
  .card--back { top: 520px; background: var(--card-dark-back); }

  /* front: white info panel */
  .info-panel { position: absolute; left: 0; top: 0; width: 100%; height: 245px; }
  .holder { position: absolute; left: 48px; top: 120px; }
  .holder__name { color: var(--accent-blue); font-size: 32px; font-weight: 400; line-height: 1; }
  .holder__title { color: var(--title-grey); font-size: 15px; margin-top: 8px; }

  .contact-list {
    position: absolute; left: 300px; top: 58px;
    list-style: none;
    border-left: 3px dotted var(--accent-blue);
    padding-left: 16px;
  }
  .contact-list li {
    display: flex; align-items: center; gap: 10px;
    color: var(--text-grey); font-size: 16px; height: 31px;
  }
  .contact-list svg { width: 18px; height: 18px; flex: none; }

  /* front: accent stripe and dark band */
  .accent-stripe { position: absolute; left: 0; top: 245px; width: 100%; height: 7px; background: var(--accent-blue); }
  .dark-band { position: absolute; left: 0; top: 252px; width: 100%; height: 159px; background: var(--card-dark); }

  .brand {
    position: absolute; display: flex; align-items: center;
    color: var(--logo-white); font-weight: 600; letter-spacing: 2px;
  }
  .brand__dot { border: 3px solid var(--logo-white); border-radius: 50%; flex: none; }
  .brand--small { left: 40px; top: 60px; gap: 12px; font-size: 22px; }
  .brand--small .brand__dot { width: 40px; height: 40px; }

  .emboss-name {
    position: absolute; left: 300px; top: 34px;
    color: var(--emboss); font-size: 74px; font-weight: 600; letter-spacing: 4px; line-height: 1;
  }

  /* back */
  .back-texture { position: absolute; inset: 0; background: var(--card-dark-back); }
  .brand--large { left: 60px; top: 162px; gap: 22px; font-size: 46px; letter-spacing: 4px; }
  .brand--large .brand__dot { width: 96px; height: 96px; border-width: 8px; }
</style>
</head>
<body>

<section class="card card--front" aria-label="Business card front">
  <div class="info-panel">
    <div class="holder">
      <h1 class="holder__name">Dana Welmore</h1>
      <p class="holder__title">Co-Founder</p>
    </div>
    <ul class="contact-list">
      <li>
        <svg viewBox="0 0 20 20"><path d="M10 1a6 6 0 0 0-6 6c0 4.5 6 12 6 12s6-7.5 6-12a6 6 0 0 0-6-6zm0 8.5A2.5 2.5 0 1 1 10 4.5a2.5 2.5 0 0 1 0 5z" fill="var(--accent-blue)"/></svg>
        2750 Marlow Avenue Suite 410 Fernvale, IL 60914
      </li>
      <li>
        <svg viewBox="0 0 20 20"><path d="M2 8c0-3 4-5 8-5s8 2 8 5h-4V6.5H6V8zM5 9h10l2 8H3z" fill="var(--accent-blue)"/></svg>
        312.555.0182
      </li>
      <li>
        <svg viewBox="0 0 20 20"><rect x="5" y="1" width="10" height="18" rx="2" fill="var(--accent-blue)"/><rect x="7" y="4" width="6" height="9" fill="#fff"/></svg>
        630.555.0147
      </li>
      <li>
        <svg viewBox="0 0 20 20"><rect x="1" y="4" width="18" height="12" fill="var(--accent-blue)"/><path d="M1 4l9 7 9-7" fill="none" stroke="#fff" stroke-width="1.5"/></svg>
        dw@crestlineholdingsllc.example
      </li>
      <li>
        <svg viewBox="0 0 20 20"><circle cx="10" cy="10" r="9" fill="var(--accent-blue)"/><path d="M1 10h18M10 1c-4 4-4 14 0 18M10 1c4 4 4 14 0 18" fill="none" stroke="#fff" stroke-width="1"/></svg>
        http://www.crestlineholdingsllc.example
      </li>
    </ul>
  </div>
  <div class="accent-stripe"></div>
  <div class="dark-band">
    <div class="emboss-name" aria-hidden="true">CRESTLINE</div>
    <div class="brand brand--small">
      <span class="brand__dot"></span>
      <span class="brand__name">CRESTLINE HOLDINGS</span>
    </div>
  </div>
</section>

<section class="card card--back" aria-label="Business card back">
  <div class="back-texture" role="img" aria-label="Fine diagonal pinstripe texture on dark charcoal"></div>
  <div class="brand brand--large">
    <span class="brand__dot"></span>
    <span class="brand__name">CRESTLINE HOLDINGS</span>
  </div>
</section>

</body>
</html>
```